trading data display webpage

We have build a rough wireframe of the two webpages that we want to display .The two wireframes are attached as a pdf document.
there will be login page. after login , the user will see the index page. that is the first page of the wireframe.

what we are displaying is essentially spread data. we are taking the difference in prices are two places and displaying the data. some calculations are done and is shown in the grid.

below the grid we show the behaviour on a graph. we will use bubble chart. I did not find a sample, hence have thrown in a placeholder.

this is time series data ( changes daily) and hence we need to check the behaviour.

the second wire frame shows how the user will choose the source price points and the destination price points.
we are talking here of natural gas prices hence the reference to source prices and destination prices.

you need to design the page/ pages such that the end-user loves it and is easy to use. the intent here is easy to use and easy to understand.
this will be responsive webpage since the end user will check it out on a tablet or a smartphone.

so if possible tell us how the navigation bar, the button bar, etc should fall when the screen size decreases.

I have uploaded 2 files. one is the wireframe ( pdf document) and second is the logo file.

please also let us know where to place the logo.

Target Market(s)

the target market is traders and data analyst

Industry/Entity Type

Build

Colors

Designer to choose colors to be used in the design.

Requirements
Must have
• 1. design for the web.
2. but think how the design will look when the screen size decreases.
3. tell if possible what screen components to keep and what to hide.

```html
<!DOCTYPE html>
<html lang="en">
<head>
<meta charset="utf-8">
<title>Gasline – Spread Data Web &amp; Mobile Screens</title>
<link rel="stylesheet" href="https://fonts.googleapis.com/css2?family=Open+Sans:wght@400;600;700&display=swap">
<style>
:root{
  --ink:#1b1b1b;
  --grey-text:#5a5d62;
  --soft-text:#8a8d92;
  --chrome:#e3e6eb;
  --band:#e8eaee;
  --line:#c4c8ce;
  --field:#ffffff;
  --field-edge:#a9adb3;
  --btn-grey:#a3a6ab;
  --btn-dark:#7d8085;
  --row-alt:#c7c9cc;
  --accent:#14a5e3;
  --accent-soft:#b8dcf3;
  --bar1:#b5dcf5;
  --bar2:#8fd0f3;
  --bar3:#3ec2ef;
  --bar4:#0aa6e5;
  --bar5:#0f77a3;
  --pie-main:#26a9e6;
  --pie-slice:#8fcbef;
  --status:#3b3c3f;
  --list:#74777c;
  --list-panel:#9a9da2;
}
*{box-sizing:border-box;margin:0;padding:0}
html,body{width:1200px;height:1000px;overflow:hidden;background:#fff}
body{position:relative;font-family:"Open Sans",Arial,sans-serif;color:var(--ink)}
.abs{position:absolute}

.board-title{position:absolute;font-weight:400;font-size:31px;line-height:36px;color:var(--ink)}
.board-title--web{left:33px;top:50px;width:380px}
.board-title--mobile{left:538px;top:42px;font-size:30px;line-height:35px}

.brand{position:absolute;display:flex;align-items:center;gap:4px;font-weight:700;color:var(--accent);font-size:11px;white-space:nowrap}
.brand__dot{width:10px;height:10px;border-radius:50%;background:var(--accent)}

.site{position:absolute;background:var(--band);overflow:hidden}
.site__header{position:absolute;left:0;top:0;right:0;height:37px;background:var(--chrome);border-bottom:1px solid var(--line)}
.site__nav{position:absolute;top:10px;font-size:5px;color:var(--grey-text);font-weight:600}
.site__nav span{position:absolute;white-space:nowrap}
.social{position:absolute;width:9px;height:9px;border-radius:50%;background:var(--accent)}
.search-label{position:absolute;font-size:4.5px;color:var(--grey-text);font-weight:600}
.search-field{position:absolute;height:9px;background:#fff;border:1px solid var(--field-edge);border-radius:2px}
.search-field::before{content:"";position:absolute;left:0;top:0;width:11px;height:100%;background:var(--accent)}

.hero{position:absolute;left:0;top:37px;width:475px;height:176px;
  background:linear-gradient(120deg,#1d3a2a 0%,#6aa52b 22%,#e8d521 38%,#f08a1c 50%,#2d8f8a 64%,#1f5fa5 78%,#b4c52e 100%)}
.hero__veil{position:absolute;left:-30px;top:55px;width:280px;height:170px;border-radius:50%;background:rgba(255,255,255,.18)}
.hero__title{position:absolute;left:23px;color:#fff;font-size:14px;font-weight:700}
.hero__text{position:absolute;left:23px;width:200px;color:#fff;font-size:8.4px;font-weight:600;line-height:10px}
.pill{position:absolute;height:9px;border-radius:2px;background:var(--btn-grey);color:#fff;font-size:4.2px;font-weight:700;display:flex;align-items:center;padding-left:4px;gap:3px;white-space:nowrap}
.pill::after{content:"";border-left:3px solid #fff;border-top:2px solid transparent;border-bottom:2px solid transparent}

.login-card{position:absolute;background:#c6c9ce;border:2px solid #a6a9ae;border-radius:3px}
.field-label{position:absolute;font-size:4.6px;color:var(--grey-text)}
.field{position:absolute;background:var(--field);border:1px solid var(--field-edge);border-radius:2px}
.check{position:absolute;width:6px;height:6px;background:#fff;border:1px solid var(--field-edge)}
.check-text{position:absolute;font-size:4.6px;color:var(--grey-text)}
.mini-links{position:absolute;font-size:3.4px;font-weight:700;color:var(--grey-text);white-space:nowrap}

.feature{position:absolute;top:228px;width:145px}
.feature__icon{position:absolute;left:0;top:0;width:28px;height:28px;border-radius:50%;background:var(--accent)}
.feature__title{position:absolute;left:36px;top:2px;font-size:16px;font-weight:700;color:var(--grey-text);white-space:nowrap}
.feature__text{position:absolute;left:0;top:40px;width:145px;font-size:7px;line-height:8.8px;color:var(--grey-text)}
.feature__divider{position:absolute;top:232px;width:1px;height:70px;background:var(--line)}

.tab{position:absolute;height:17px;border-radius:4px 10px 0 0;font-size:6px;font-weight:700;display:flex;align-items:center;justify-content:center;color:#fff;background:#b9bcc0}
.tab--active{background:var(--accent)}
.panel{position:absolute;background:var(--accent-soft);border-radius:0 0 10px 10px}
.card{position:absolute;background:#fff}
.select{position:absolute;height:12px;background:#fff;border:1px solid var(--field-edge);border-radius:1px;font-size:6px;color:var(--grey-text);padding-left:4px;line-height:10px;white-space:nowrap}
.select::after{content:"";position:absolute;right:0;top:0;width:9px;height:100%;background:#e5e6e8;border-left:1px solid var(--field-edge)}
.chip-row{position:absolute;display:flex;gap:3px}
.chip{height:12px;background:var(--btn-grey);color:#fff;font-size:5px;font-weight:700;display:flex;align-items:center;justify-content:center;border-radius:1px;white-space:nowrap}

.grid{position:absolute;display:grid;gap:2px}
.grid__head{height:16px;background:var(--btn-dark);color:#fff;font-size:5px;font-weight:700;display:flex;align-items:center;padding-left:3px;white-space:nowrap}
.grid__cell{height:17px;background:#fff;border:1px solid var(--line);font-size:6px;color:var(--grey-text);display:flex;align-items:center;padding-left:5px}
.grid__cell--alt{background:var(--row-alt)}

.legend{position:absolute;font-size:5.5px;color:var(--grey-text);display:flex;align-items:center;gap:4px}
.legend i{display:block;width:7px;height:7px}
.axis-label{position:absolute;font-size:5px;color:var(--grey-text);font-weight:600}

.screen{position:absolute;width:156px;height:240px;background:var(--band);overflow:hidden}
.status{position:absolute;left:0;top:0;width:100%;height:14px;background:var(--status)}
.status__signal{position:absolute;left:6px;top:4px}
.screen__logo{position:absolute;left:5px;top:19px}
.burger{position:absolute;right:6px;top:22px;width:13px}
.burger i{display:block;height:1.5px;background:var(--grey-text);margin-bottom:2.2px}
.m-tabs{position:absolute;left:0;top:42px;width:156px;height:18px;border-bottom:4px solid var(--accent)}
.m-tab{position:absolute;top:0;height:14px;width:48px;font-size:5px;font-weight:700;color:#fff;background:#b9bcc0;border-radius:3px 8px 0 0;display:flex;align-items:center;justify-content:center}
.m-tab--active{background:var(--accent)}
.m-body{position:absolute;left:0;top:60px;width:156px;bottom:0;background:#fff}
.m-label{position:absolute;font-size:5.5px;color:var(--grey-text);white-space:nowrap}
.m-btn{position:absolute;height:13px;background:var(--accent);color:#fff;font-size:5px;font-weight:700;display:flex;align-items:center;justify-content:center}
.login-btn{position:absolute;height:14px;background:var(--btn-grey);color:#fff;font-size:6px;font-weight:700;display:flex;align-items:center;padding-left:6px;gap:5px;border-radius:1px}
.login-btn::after{content:"";border-left:4px solid #fff;border-top:3px solid transparent;border-bottom:3px solid transparent}

.overlay{position:absolute;inset:14px 0 0 0;background:rgba(60,62,66,.55)}
.sheet{position:absolute;background:var(--list-panel);border-radius:3px;padding:4px}
.sheet__title{font-size:5.5px;color:#ececec;padding:2px 3px 3px}
.sheet__item{height:12.2px;margin-bottom:3px;background:var(--list);color:#fff;font-size:5.6px;display:flex;align-items:center;padding-left:4px;white-space:nowrap}
.round-btn{position:absolute;width:18px;height:18px;border-radius:50%;background:var(--accent);border:2px solid #fff}

.action{position:absolute;text-align:center;font-size:5px;font-weight:600;color:var(--grey-text);white-space:nowrap}
.action svg{display:block;margin:0 auto 6px}
.faded{opacity:.4}

.m-grid{position:absolute;left:9px;top:78px;display:grid;grid-template-columns:46px 92px;gap:1.5px}
.m-grid .grid__head{height:11px;font-size:4.2px}
.m-grid .grid__cell{height:14px;font-size:5px}
.swipe{position:absolute;left:13px;top:173px;font-size:4.8px;font-style:italic;color:var(--grey-text)}
.chart-title{position:absolute;left:12px;top:77px;font-size:6px;color:var(--grey-text)}
</style>
</head>
<body>

<h1 class="board-title board-title--web">WEBSITE PAGE - Log-in &amp; Landing</h1>
<h2 class="board-title board-title--mobile">Mobile Pages - Log-in, Landing, Index Selection Table/Data, Chart Selection, Chart Page</h2>

<!-- Website: log-in & landing -->
<section class="site" style="left:37px;top:135px;width:475px;height:325px">
  <header class="site__header">
    <div class="brand" style="left:14px;top:12px"><span class="brand__dot"></span>Gasline</div>
    <nav class="site__nav" style="left:0;top:11px">
      <span style="left:266px">HOME</span>
      <span style="left:299px">WHAT WE DO</span>
      <span style="left:348px">THE TEAM</span>
      <span style="left:389px">CONTACT US</span>
    </nav>
    <span class="social" style="left:427px;top:8px"></span>
    <span class="social" style="left:439px;top:8px"></span>
    <span class="social" style="left:451px;top:8px"></span>
    <span class="search-label" style="left:377px;top:23px">SEARCH</span>
    <span class="search-field" style="left:402px;top:21px;width:58px"></span>
  </header>

  <div class="hero" role="img" aria-label="Photograph of tightly rolled coloured paper spirals in green, yellow, orange and blue"></div>
  <div class="hero__veil"></div>
  <div class="hero__title" style="top:153px">Lorem Ipsum</div>
  <p class="hero__text" style="top:171px">Lorem ipsum dolor sit amet, consectetur adipisicing elit, sed do eiusmod.</p>
  <span class="pill" style="left:172px;top:196px;width:36px">READ MORE</span>

  <div class="login-card" style="left:353px;top:58px;width:118px;height:120px">
    <div class="brand" style="left:32px;top:10px;font-size:10px"><span class="brand__dot"></span>Gasline</div>
    <span class="field-label" style="left:14px;top:38px">Username</span>
    <span class="field" style="left:14px;top:45px;width:80px;height:9px"></span>
    <span class="field-label" style="left:14px;top:57px">Password</span>
    <span class="field" style="left:14px;top:64px;width:80px;height:9px"></span>
    <span class="check" style="left:14px;top:83px"></span>
    <span class="check-text" style="left:23px;top:83px">Remember Me</span>
    <span class="pill" style="left:62px;top:82px;width:32px;background:#9a9da2">LOG IN</span>
    <span class="abs" style="left:14px;top:97px;width:84px;height:1px;background:#a9acb1"></span>
    <span class="mini-links" style="left:20px;top:103px">REGISTER HERE &nbsp;|&nbsp; FORGOT PASSWORD</span>
  </div>

  <div class="feature" style="left:22px">
    <span class="feature__icon"><svg width="28" height="28" viewBox="0 0 28 28"><polyline points="7,18 12,12 15,15 21,9" fill="none" stroke="#fff" stroke-width="2"/><circle cx="21" cy="9" r="1.6" fill="#fff"/></svg></span>
    <span class="feature__title">Services</span>
    <p class="feature__text">Lorem ipsum dolor sit amet, consectetur adipisicing elit, sed do eiusmod tempor incididunt ut labore et dolore magna aliquam.</p>
  </div>
  <span class="feature__divider" style="left:165px"></span>
  <div class="feature" style="left:177px">
    <span class="feature__icon"><svg width="28" height="28" viewBox="0 0 28 28"><circle cx="14" cy="9" r="3" fill="#fff"/><rect x="11" y="13" width="6" height="8" rx="2" fill="#fff"/><circle cx="8" cy="11" r="2.2" fill="#fff"/><rect x="6" y="14" width="4" height="6" rx="1.5" fill="#fff"/><circle cx="20" cy="11" r="2.2" fill="#fff"/><rect x="18" y="14" width="4" height="6" rx="1.5" fill="#fff"/></svg></span>
    <span class="feature__title">The Team</span>
    <p class="feature__text">Lorem ipsum dolor sit amet, consectetur adipisicing elit, sed do eiusmod tempor incididunt ut labore et dolore magna aliquam.</p>
  </div>
  <span class="feature__divider" style="left:322px"></span>
  <div class="feature" style="left:335px">
    <span class="feature__icon"><svg width="28" height="28" viewBox="0 0 28 28"><rect x="7" y="9" width="14" height="10" fill="#fff"/><polyline points="7,9 14,15 21,9" fill="none" stroke="#14a5e3" stroke-width="1.4"/></svg></span>
    <span class="feature__title">Contact Us</span>
    <p class="feature__text">Lorem ipsum dolor sit amet, consectetur adipisicing elit, sed do eiusmod tempor incididunt ut labore et dolore magna aliquam.</p>
  </div>
  <span class="pill" style="left:111px;top:301px;width:42px">READ MORE</span>
  <span class="pill" style="left:268px;top:301px;width:42px">READ MORE</span>
  <span class="pill" style="left:422px;top:301px;width:42px">READ MORE</span>
</section>

<!-- Website: spread dashboard -->
<section class="site" style="left:32px;top:493px;width:474px;height:444px">
  <header class="site__header">
    <div class="brand" style="left:14px;top:12px"><span class="brand__dot"></span>Gasline</div>
    <nav class="site__nav" style="left:0;top:11px">
      <span style="left:266px">HOME</span>
      <span style="left:298px">WHAT WE DO</span>
      <span style="left:348px">THE TEAM</span>
      <span style="left:390px">CONTACT US</span>
    </nav>
    <span class="social" style="left:427px;top:8px"></span>
    <span class="social" style="left:439px;top:8px"></span>
    <span class="social" style="left:451px;top:8px"></span>
    <span class="search-label" style="left:377px;top:23px">SEARCH</span>
    <span class="search-field" style="left:402px;top:21px;width:58px"></span>
  </header>

  <span class="tab tab--active" style="left:18px;top:64px;width:66px">EAST</span>
  <span class="tab" style="left:84px;top:64px;width:66px">CENTRAL</span>
  <span class="tab" style="left:150px;top:64px;width:66px">WEST</span>

  <div class="panel" style="left:18px;top:80px;width:438px;height:337px"></div>

  <div class="card" style="left:31px;top:90px;width:414px;height:174px">
    <span class="select" style="left:9px;top:6px;width:123px">Source Indices</span>
    <span class="select" style="left:284px;top:6px;width:122px">Destination Indices</span>
    <div class="chip-row" style="left:9px;top:25px">
      <span class="chip" style="width:38px">5 DAYS</span>
      <span class="chip" style="width:38px">7 DAYS</span>
      <span class="chip" style="width:46px">15 DAYS</span>
    </div>
    <span class="select" style="left:284px;top:25px;width:59px">Month</span>
    <span class="select" style="left:347px;top:25px;width:59px">Year</span>

    <div class="grid" style="left:8px;top:48px;grid-template-columns:repeat(7,55px)">
      <span class="grid__head">Spread Name</span><span class="grid__head">Average Spread</span><span class="grid__head">+ve prob</span><span class="grid__head">-ve prob</span><span class="grid__head">Spike Prob</span><span class="grid__head">Average Supply</span><span class="grid__head">Supply Cut_Prob</span>
      <span class="grid__cell">Spread 1</span><span class="grid__cell"></span><span class="grid__cell"></span><span class="grid__cell"></span><span class="grid__cell"></span><span class="grid__cell"></span><span class="grid__cell"></span>
      <span class="grid__cell grid__cell--alt">Spread 2</span><span class="grid__cell grid__cell--alt"></span><span class="grid__cell grid__cell--alt"></span><span class="grid__cell grid__cell--alt"></span><span class="grid__cell grid__cell--alt"></span><span class="grid__cell grid__cell--alt"></span><span class="grid__cell grid__cell--alt"></span>
      <span class="grid__cell">Spread 3</span><span class="grid__cell"></span><span class="grid__cell"></span><span class="grid__cell"></span><span class="grid__cell"></span><span class="grid__cell"></span><span class="grid__cell"></span>
      <span class="grid__cell grid__cell--alt">Spread 4</span><span class="grid__cell grid__cell--alt"></span><span class="grid__cell grid__cell--alt"></span><span class="grid__cell grid__cell--alt"></span><span class="grid__cell grid__cell--alt"></span><span class="grid__cell grid__cell--alt"></span><span class="grid__cell grid__cell--alt"></span>
      <span class="grid__cell">Spread 5</span><span class="grid__cell"></span><span class="grid__cell"></span><span class="grid__cell"></span><span class="grid__cell"></span><span class="grid__cell"></span><span class="grid__cell"></span>
    </div>
  </div>

  <div class="card" style="left:31px;top:278px;width:201px;height:122px">
    <span class="select" style="left:10px;top:10px;width:121px">Supply Vs Demand</span>
    <svg class="abs" style="left:56px;top:38px" width="76" height="76" viewBox="0 0 76 76">
      <circle cx="38" cy="38" r="37" fill="var(--pie-main)"/>
      <path d="M38 38 L38 1 A37 37 0 0 1 61 67 Z" fill="var(--pie-slice)"/>
    </svg>
    <span class="legend" style="left:148px;top:52px"><i style="background:var(--pie-main)"></i>Item 1</span>
    <span class="legend" style="left:148px;top:63px"><i style="background:var(--pie-slice)"></i>Item 2</span>
  </div>

  <div class="card" style="left:243px;top:278px;width:201px;height:122px">
    <span class="select" style="left:10px;top:10px;width:121px">Supply Across Time</span>
    <svg class="abs" style="left:24px;top:28px" width="170" height="70" viewBox="0 0 170 70">
      <line x1="1" y1="0" x2="1" y2="70" stroke="#b0b3b8"/>
      <line x1="1" y1="69.5" x2="170" y2="69.5" stroke="#b0b3b8"/>
      <rect x="6" y="36" width="22" height="33" fill="var(--bar1)"/>
      <rect x="35" y="26" width="22" height="43" fill="var(--bar2)"/>
      <rect x="64" y="12" width="22" height="57" fill="var(--bar3)"/>
      <rect x="93" y="36" width="22" height="33" fill="var(--bar4)"/>
      <rect x="122" y="22" width="22" height="47" fill="var(--bar5)"/>
    </svg>
    <span class="axis-label" style="left:29px;top:102px">Item 1</span>
    <span class="axis-label" style="left:58px;top:102px">Item 2</span>
    <span class="axis-label" style="left:87px;top:102px">Item 3</span>
    <span class="axis-label" style="left:116px;top:102px">Item 4</span>
    <span class="axis-label" style="left:145px;top:102px">Item 5</span>
  </div>
</section>

<!-- Mobile: log-in -->
<section class="screen" style="left:553px;top:190px">
  <div class="status"><svg class="status__signal" width="16" height="6"><rect x="0" y="4" width="2" height="2" fill="#ccc"/><rect x="3" y="3" width="2" height="3" fill="#ccc"/><rect x="6" y="2" width="2" height="4" fill="#ccc"/><rect x="9" y="1" width="2" height="5" fill="#ccc"/><rect x="12" y="0" width="2" height="6" fill="#ccc"/></svg></div>
  <div class="brand" style="left:44px;top:58px;font-size:14px"><span class="brand__dot" style="width:14px;height:14px"></span>Gasline</div>
  <span class="m-label" style="left:20px;top:95px;font-size:6.5px">Username</span>
  <span class="field" style="left:20px;top:106px;width:128px;height:17px"></span>
  <span class="m-label" style="left:20px;top:129px;font-size:6.5px">Password</span>
  <span class="field" style="left:20px;top:139px;width:128px;height:17px"></span>
  <span class="check" style="left:20px;top:165px;width:9px;height:9px"></span>
  <span class="m-label" style="left:34px;top:165px;font-size:6.5px">Remember Me</span>
  <span class="login-btn" style="left:102px;top:181px;width:46px">LOG IN</span>
  <span class="abs" style="left:18px;top:200px;width:132px;height:1px;background:#a9acb1"></span>
  <span class="m-label" style="left:30px;top:208px;font-size:4.6px;font-weight:700">REGISTER HERE &nbsp;|&nbsp; FORGOT PASSWORD</span>
</section>

<!-- Mobile: landing / selection -->
<section class="screen" style="left:774px;top:190px">
  <div class="status"><svg class="status__signal" width="16" height="6"><rect x="0" y="4" width="2" height="2" fill="#ccc"/><rect x="3" y="3" width="2" height="3" fill="#ccc"/><rect x="6" y="2" width="2" height="4" fill="#ccc"/><rect x="9" y="1" width="2" height="5" fill="#ccc"/><rect x="12" y="0" width="2" height="6" fill="#ccc"/></svg></div>
  <div class="brand screen__logo" style="font-size:7px"><span class="brand__dot" style="width:7px;height:7px"></span>Gasline</div>
  <div class="burger"><i></i><i></i><i></i></div>
  <div class="m-tabs"><span class="m-tab m-tab--active" style="left:0">EAST</span><span class="m-tab" style="left:48px">CENTRAL</span><span class="m-tab" style="left:96px">WEST</span></div>
  <div class="m-body">
    <span class="m-label" style="left:22px;top:15px">SOURCE INDICES</span>
    <span class="select" style="left:20px;top:24px;width:110px;height:11px"></span>
    <span class="m-label" style="left:22px;top:47px">DESTINATION INDICES</span>
    <span class="select" style="left:20px;top:57px;width:110px;height:11px"></span>
    <span class="m-label" style="left:22px;top:76px">TERM</span>
    <div class="chip-row" style="left:20px;top:86px;gap:2px">
      <span class="chip" style="width:35px;height:10px;font-size:4px">5 DAYS</span>
      <span class="chip" style="width:35px;height:10px;font-size:4px">7 DAYS</span>
      <span class="chip" style="width:36px;height:10px;font-size:4px">15 DAYS</span>
    </div>
    <span class="m-label" style="left:22px;top:104px">MONTH</span>
    <span class="m-label" style="left:78px;top:104px">YEAR</span>
    <span class="select" style="left:20px;top:113px;width:52px;height:11px"></span>
    <span class="select" style="left:77px;top:113px;width:53px;height:11px"></span>
    <span class="m-btn" style="left:20px;top:144px;width:110px">GENERATE TABLE</span>
  </div>
</section>

<!-- Mobile: index selection -->
<section class="screen" style="left:994px;top:190px">
  <div class="status"><svg class="status__signal" width="16" height="6"><rect x="0" y="4" width="2" height="2" fill="#ccc"/><rect x="3" y="3" width="2" height="3" fill="#ccc"/><rect x="6" y="2" width="2" height="4" fill="#ccc"/><rect x="9" y="1" width="2" height="5" fill="#ccc"/><rect x="12" y="0" width="2" height="6" fill="#ccc"/></svg></div>
  <div class="brand screen__logo faded" style="font-size:7px"><span class="brand__dot" style="width:7px;height:7px"></span>Gasline</div>
  <div class="overlay"></div>
  <div class="sheet" style="left:4px;top:22px;width:148px;height:208px">
    <div class="sheet__title">SELECT A SOURCE INDEX</div>
    <div class="sheet__item">Harbor Point Hub</div>
    <div class="sheet__item">Cedar Valley</div>
    <div class="sheet__item">Stone Creek North</div>
    <div class="sheet__item">Stone Creek South</div>
    <div class="sheet__item">Pine Ridge Inlet</div>
    <div class="sheet__item">Pine Ridge Zone 2</div>
    <div class="sheet__item">Maple Bend</div>
    <div class="sheet__item">Coastal Link</div>
    <div class="sheet__item">Eastfield Exit</div>
    <div class="sheet__item">Bluewater Hub</div>
    <div class="sheet__item">Granite Pass A</div>
    <div class="sheet__item" style="width:78px">Granite Pass B</div>
  </div>
  <span class="round-btn" style="left:64px;top:211px"><svg width="14" height="14" viewBox="0 0 14 14"><polygon points="3,4 11,4 7,10" fill="#fff"/></svg></span>
</section>

<!-- Mobile: table / data -->
<section class="screen" style="left:553px;top:597px">
  <div class="status"><svg class="status__signal" width="16" height="6"><rect x="0" y="4" width="2" height="2" fill="#ccc"/><rect x="3" y="3" width="2" height="3" fill="#ccc"/><rect x="6" y="2" width="2" height="4" fill="#ccc"/><rect x="9" y="1" width="2" height="5" fill="#ccc"/><rect x="12" y="0" width="2" height="6" fill="#ccc"/></svg></div>
  <div class="brand screen__logo" style="font-size:7px"><span class="brand__dot" style="width:7px;height:7px"></span>Gasline</div>
  <div class="burger"><i></i><i></i><i></i></div>
  <div class="m-tabs"><span class="m-tab m-tab--active" style="left:0">EAST</span><span class="m-tab" style="left:48px">CENTRAL</span><span class="m-tab" style="left:96px">WEST</span></div>
  <div class="m-body"></div>
  <div class="m-grid">
    <span class="grid__head">Spread Name</span><span class="grid__head" style="justify-content:center">Average Spread</span>
    <span class="grid__cell">Spread 1</span><span class="grid__cell"></span>
    <span class="grid__cell grid__cell--alt">Spread 2</span><span class="grid__cell grid__cell--alt"></span>
    <span class="grid__cell">Spread 3</span><span class="grid__cell"></span>
    <span class="grid__cell grid__cell--alt">Spread 4</span><span class="grid__cell grid__cell--alt"></span>
    <span class="grid__cell">Spread 5</span><span class="grid__cell"></span>
  </div>
  <span class="round-btn" style="left:131px;top:112px;width:22px;height:22px"><svg width="18" height="18" viewBox="0 0 18 18"><polygon points="7,5 13,9 7,13" fill="#fff"/></svg></span>
  <span class="swipe">Swipe to view more data.</span>
  <div class="action" style="left:26px;top:186px"><svg width="22" height="22" viewBox="0 0 22 22"><path d="M17 11 A6 6 0 1 1 11 5" fill="none" stroke="#8a8d92" stroke-width="3"/><polygon points="10,0 16,5 10,10" fill="#8a8d92"/></svg>REDO</div>
  <div class="action" style="left:69px;top:186px"><svg width="30" height="22" viewBox="0 0 30 22"><rect x="4" y="12" width="6" height="10" fill="#8a8d92"/><rect x="12" y="6" width="6" height="16" fill="#8a8d92"/><rect x="20" y="0" width="6" height="22" fill="#8a8d92"/></svg>GENERATE CHART</div>
</section>

<!-- Mobile: chart selection -->
<section class="screen" style="left:774px;top:597px">
  <div class="status"><svg class="status__signal" width="16" height="6"><rect x="0" y="4" width="2" height="2" fill="#ccc"/><rect x="3" y="3" width="2" height="3" fill="#ccc"/><rect x="6" y="2" width="2" height="4" fill="#ccc"/><rect x="9" y="1" width="2" height="5" fill="#ccc"/><rect x="12" y="0" width="2" height="6" fill="#ccc"/></svg></div>
  <div class="brand screen__logo faded" style="font-size:7px"><span class="brand__dot" style="width:7px;height:7px"></span>Gasline</div>
  <div class="burger faded"><i></i><i></i><i></i></div>
  <div class="m-tabs faded"><span class="m-tab m-tab--active" style="left:0">EAST</span><span class="m-tab" style="left:48px">CENTRAL</span><span class="m-tab" style="left:96px">WEST</span></div>
  <div class="m-body"></div>
  <div class="sheet" style="left:4px;top:67px;width:148px;height:120px">
    <div class="sheet__title">SELECT A CHART</div>
    <div class="sheet__item">Chart 1</div>
    <div class="sheet__item">Chart 2</div>
    <div class="sheet__item">Chart 3</div>
    <div class="sheet__item">Chart 4</div>
    <div class="sheet__item">Chart 5</div>
    <div class="sheet__item">Chart 6</div>
  </div>
  <div class="action faded" style="left:33px;top:186px"><svg width="22" height="22" viewBox="0 0 22 22"><path d="M17 11 A6 6 0 1 1 11 5" fill="none" stroke="#8a8d92" stroke-width="3"/><polygon points="10,0 16,5 10,10" fill="#8a8d92"/></svg>REDO</div>
  <div class="action faded" style="left:74px;top:186px"><svg width="30" height="22" viewBox="0 0 30 22"><rect x="4" y="12" width="6" height="10" fill="#8a8d92"/><rect x="12" y="6" width="6" height="16" fill="#8a8d92"/><rect x="20" y="0" width="6" height="22" fill="#8a8d92"/></svg>GENERATE CHART</div>
</section>

<!-- Mobile: chart page -->
<section class="screen" style="left:994px;top:597px">
  <div class="status"><svg class="status__signal" width="16" height="6"><rect x="0" y="4" width="2" height="2" fill="#ccc"/><rect x="3" y="3" width="2" height="3" fill="#ccc"/><rect x="6" y="2" width="2" height="4" fill="#ccc"/><rect x="9" y="1" width="2" height="5" fill="#ccc"/><rect x="12" y="0" width="2" height="6" fill="#ccc"/></svg></div>
  <div class="brand screen__logo" style="font-size:7px"><span class="brand__dot" style="width:7px;height:7px"></span>Gasline</div>
  <div class="burger"><i></i><i></i><i></i></div>
  <div class="m-tabs"><span class="m-tab m-tab--active" style="left:0">EAST</span><span class="m-tab" style="left:48px">CENTRAL</span><span class="m-tab" style="left:96px">WEST</span></div>
  <div class="m-body"></div>
  <span class="chart-title">SUPPLY ACROSS TIME</span>
  <svg class="abs" style="left:12px;top:96px" width="130" height="60" viewBox="0 0 130 60">
    <line x1="0.5" y1="0" x2="0.5" y2="60" stroke="#b0b3b8"/>
    <line x1="0" y1="59.5" x2="130" y2="59.5" stroke="#b0b3b8"/>
    <rect x="5" y="31" width="19" height="28" fill="var(--bar1)"/>
    <rect x="29" y="22" width="19" height="37" fill="var(--bar2)"/>
    <rect x="54" y="9" width="19" height="50" fill="var(--bar3)"/>
    <rect x="79" y="31" width="19" height="28" fill="var(--bar4)"/>
    <rect x="104" y="18" width="19" height="41" fill="var(--bar5)"/>
  </svg>
  <span class="axis-label" style="left:16px;top:161px;font-size:4.2px">Item 1</span>
  <span class="axis-label" style="left:40px;top:161px;font-size:4.2px">Item 2</span>
  <span class="axis-label" style="left:65px;top:161px;font-size:4.2px">Item 3</span>
  <span class="axis-label" style="left:90px;top:161px;font-size:4.2px">Item 4</span>
  <span class="axis-label" style="left:115px;top:161px;font-size:4.2px">Item 5</span>
  <div class="action" style="left:16px;top:186px"><svg width="22" height="22" viewBox="0 0 22 22"><path d="M17 11 A6 6 0 1 1 11 5" fill="none" stroke="#8a8d92" stroke-width="3"/><polygon points="10,0 16,5 10,10" fill="#8a8d92"/></svg>REDO</div>
  <div class="action" style="left:56px;top:188px"><svg width="32" height="20" viewBox="0 0 32 20"><g fill="#8a8d92"><rect x="0" y="0" width="9" height="5"/><rect x="11" y="0" width="10" height="5"/><rect x="23" y="0" width="9" height="5"/><rect x="0" y="7" width="9" height="5"/><rect x="11" y="7" width="10" height="5"/><rect x="23" y="7" width="9" height="5"/><rect x="0" y="14" width="9" height="5"/><rect x="11" y="14" width="10" height="5"/><rect x="23" y="14" width="9" height="5"/></g></svg>VIEW TABLE</div>
  <div class="action" style="left:106px;top:186px"><svg width="26" height="22" viewBox="0 0 26 22"><rect x="2" y="12" width="6" height="10" fill="#8a8d92"/><rect x="10" y="6" width="6" height="16" fill="#8a8d92"/><rect x="18" y="0" width="6" height="22" fill="#8a8d92"/></svg>OTHER CHARTS</div>
</section>

</body>
</html>
```